Corporate flyer introducing a brand new technology apprenticeship program in Australia!

A professional, yet clean and contemporary looking flyer to advertise a brand new service offering in a simple, easy to read format with engaging images. Here is a link to our current online brochure which outlines the program we would like to advertise in a hardcopy flyer/brochure format: https://pages.vendrap.com/Information-on-Technology-Higher-Apprenticeships-for-Employers-Victoria-kT3pzqW7LmRe

Target Market(s)

Medium to large sized businesses involved in using cutting edge technology, such as engineering and advanced manufracturing (3D printing etc)

Industry/Entity Type

Engineering

Colors

Designer to choose colors to be used in the design.

Requirements
Must have
• Contemporary, clean looking, easy to read, tech/engineering/advanced manufacturing related imagery
Nice to have
• Some ideas about different sizes/styles (eg something other than a plain A4 sheet)
Should not have
• Unprofessional or offensive language

```html
<!DOCTYPE html>
<html lang="en">
<head>
<meta charset="utf-8">
<title>Technology Higher Apprentices 2019 Program</title>
<link href="https://fonts.googleapis.com/css2?family=Montserrat:wght@400;600;700;800&family=Open+Sans:wght@400;600;700&display=swap" rel="stylesheet">
<style>
:root{
  --orange:#e8552a;
  --orange-dark:#d1461f;
  --ink:#3a3a3a;
  --muted:#6b6b6b;
  --paper:#ffffff;
  --stage:#eeeeee;
  --photo-a:#4a5a6a;
  --photo-b:#8a96a0;
}
*{margin:0;padding:0;box-sizing:border-box}
html,body{width:1200px;height:3708px;overflow:hidden;background:var(--stage)}
body{position:relative;font-family:"Open Sans",Arial,sans-serif;color:var(--ink)}
.spread{position:absolute;left:100px;width:1000px;height:500px;display:flex;box-shadow:0 6px 18px rgba(0,0,0,.18)}
.page{position:relative;width:500px;height:500px;background:var(--paper);overflow:hidden}
.page.orange{background:var(--orange);color:#fff}
.page + .page{border-left:1px solid #e2e2e2}
.h1{font-family:"Montserrat",sans-serif;font-weight:700;color:var(--orange);font-size:26px;line-height:1.1}
.lead{font-family:"Montserrat",sans-serif;font-weight:600;font-size:12px;line-height:1.4;color:var(--ink);margin:10px 0}
p.body{font-size:8px;line-height:1.55;color:var(--muted);margin-bottom:7px}
.sub{font-weight:700;font-size:9px;color:var(--orange);margin:6px 0 4px}
.folio{position:absolute;bottom:16px;font-size:6px;letter-spacing:.6px;color:var(--orange);text-transform:uppercase}
.folio.r{right:60px}
.num{position:absolute;bottom:10px;font-family:"Montserrat",sans-serif;font-size:22px;color:#cfcfcf}
.num.l{left:30px;bottom:30px}.num.r{right:20px}
.badge{position:absolute;top:22px;right:24px;width:40px;height:40px;background:var(--orange);color:#fff;font-family:"Montserrat",sans-serif;font-weight:700;font-size:9px;display:flex;align-items:center;justify-content:center;text-align:center;line-height:1.1}
.ghost{position:absolute;border-radius:50%;border:40px solid rgba(0,0,0,.05)}
.page.orange .ghost{border-color:rgba(255,255,255,.12)}
.photo{position:absolute;background:linear-gradient(135deg,var(--photo-a),var(--photo-b))}
.brand{font-family:"Montserrat",sans-serif;font-weight:700;font-size:13px;color:#fff;display:flex;align-items:center;gap:6px}
.brand i{display:block;width:12px;height:12px;background:#fff}
.content{position:absolute;left:30px;right:30px}
.bar{background:var(--orange);color:#fff;font-weight:700;font-size:8px;padding:5px 8px;margin:8px 0 6px}
.units{display:grid;grid-template-columns:1fr 1fr;gap:4px 10px}
.units div{border:1px solid #e0e0e0;font-size:7px;padding:4px 6px;color:var(--muted)}
</style>
</head>
<body>

<!-- Cover spread -->
<section class="spread" style="top:0">
  <div class="page orange">
    <div class="content" style="top:20px;left:40px">
      <div style="font-family:Montserrat,sans-serif;font-weight:800;font-size:28px;line-height:1.05">TECHNOLOGY<br>HIGHER<br>APPRENTICES</div>
      <div style="font-family:Montserrat,sans-serif;font-weight:600;font-size:14px;margin-top:6px">2019 PROGRAM</div>
    </div>
    <div class="photo" role="img" aria-label="Photo of an engineer working with advanced manufacturing equipment" style="left:40px;top:160px;width:300px;height:220px"></div>
    <div style="position:absolute;left:40px;bottom:40px;font-size:9px;width:180px">The future of technology by the industries who need it most</div>
    <div class="brand" style="position:absolute;right:40px;bottom:40px"><i></i>Nexa Group</div>
  </div>
  <div class="page orange">
    <div class="ghost" style="width:420px;height:420px;left:60px;top:140px"></div>
    <div class="content" style="top:30px;left:150px">
      <div style="font-family:Montserrat,sans-serif;font-weight:700;font-size:18px">Let's move forward</div>
      <p style="font-size:8px;line-height:1.5;margin-top:10px">We have a placement for you before the end of the year.</p>
      <p style="font-size:8px;line-height:1.5;margin-top:6px">Your future workforce can start here. Contact our team today to discuss the program and the next intake.</p>
      <div style="font-family:Montserrat,sans-serif;font-weight:700;font-size:16px;margin-top:12px">☎ 1300 555 010</div>
    </div>
    <div class="brand" style="position:absolute;right:60px;bottom:40px"><i></i>Nexa Talent</div>
  </div>
</section>

<!-- Spread 2 -->
<section class="spread" style="top:620px">
  <div class="page orange"><div class="ghost" style="width:440px;height:440px;left:40px;top:40px"></div></div>
  <div class="page">
    <div class="badge">Industry<br>4.0</div>
    <div class="content" style="top:70px">
      <div class="h1">Technology<br>Higher Apprentices<br>Program</div>
      <div class="lead">Join industry leaders in this unique program aimed at future-proofing Australian businesses.</div>
      <p class="body">The technology higher apprenticeship combines the best of formal study and workplace learning. Apprentices gain a diploma and a degree while building real skills on the job for the businesses of tomorrow.</p>
      <p class="body">These higher apprentices are employed on a career track in a traditional apprenticeship model, but they are enrolled in a Diploma of Applied Technologies, followed by an Associate Degree in Applied Technologies with a partner university.</p>
      <p class="body">The higher apprentices are also rotating through a number of significant placements inside host businesses so they can see every part of a modern technology workplace first hand.</p>
    </div>
    <div class="folio r">The future of technology 2019 program</div><div class="num r">01</div>
  </div>
</section>

<!-- Spread 3 -->
<section class="spread" style="top:1260px">
  <div class="page">
    <div style="position:absolute;left:0;top:0;width:500px;height:60px;background:var(--orange)"></div>
    <div class="content" style="top:18px"><div class="h1" style="color:#fff;font-size:20px">What is Industry 4.0</div></div>
    <div class="content" style="top:80px">
      <p class="body">Industry 4.0 refers to the fourth industrial revolution, where connected systems, data and automation change how products are designed and built. It brings cyber-physical systems, cloud computing and smart machines into every workplace.</p>
      <p class="body">Businesses that adopt these tools need staff who understand both the technology and the process. This program builds that workforce from the ground up, inside real companies.</p>
      <p class="body">Each wave of industry has changed the skills needed by workers. The shift to Industry 4.0 asks for people who can learn quickly, solve problems and work across many fields.</p>
    </div>
    <div class="photo" role="img" aria-label="Illustration row showing the four stages of industry from steam power to connected systems" style="left:30px;top:270px;width:440px;height:90px;background:linear-gradient(90deg,#f3d6cc,#f7e4dc)"></div>
    <div style="position:absolute;left:30px;top:368px;width:440px;display:flex;gap:10px">
      <div style="flex:1;font-size:7px;color:var(--muted)"><b style="color:var(--orange)">Industry 1.0</b><br>Mechanical production powered by water and steam.</div>
      <div style="flex:1;font-size:7px;color:var(--muted)"><b style="color:var(--orange)">Industry 2.0</b><br>Mass production using electrical energy.</div>
      <div style="flex:1;font-size:7px;color:var(--muted)"><b style="color:var(--orange)">Industry 3.0</b><br>Electronics and IT automate production.</div>
      <div style="flex:1;font-size:7px;color:var(--muted)"><b style="color:var(--orange)">Industry 4.0</b><br>Connected cyber-physical systems.</div>
    </div>
    <div class="num l">02</div><div class="folio" style="left:80px">The future of technology 2019 program</div>
  </div>
  <div class="page">
    <div class="ghost" style="width:440px;height:440px;left:80px;top:160px"></div>
    <div class="badge">Industry<br>4.0</div>
    <div class="content" style="top:70px">
      <div class="h1">Industry 4.0<br>Higher Apprenticeships<br>Pilot Program</div>
      <div class="lead">The program utilises an apprenticeship framework to deliver a new Diploma and Associate Degree in Applied Technologies.</div>
      <p class="body">The pilot began in 2017 with a group of employers who wanted a new path for young talent. It joins paid work with structured study and close mentoring.</p>
      <p class="body">Apprentices learn the foundations of mechatronics, data and digital design, then apply them to real projects within their host business.</p>
    </div>
    <div class="folio r">The future of technology 2019 program</div><div class="num r">03</div>
  </div>
</section>

<!-- Spread 4 -->
<section class="spread" style="top:1900px">
  <div class="page">
    <div class="content" style="top:40px">
      <div class="h1">Current Intake</div>
      <p class="body" style="margin-top:12px">In 2018 fifteen apprentices joined the program across a range of large and mid sized employers. They came from different schools and backgrounds, all with a strong interest in technology.</p>
      <p class="body">Each apprentice works four days a week with their employer and studies one day a week, supported by a dedicated field officer.</p>
      <div class="sub">Story 1: Hands on learning</div>
      <p class="body">One of the apprentices began on the factory floor and now helps run a 3D printing cell. She says the mix of theory and practice has helped her grow faster than she expected.</p>
      <p class="body">Her employer sees the value of building skills in house and plans to take on more apprentices in the next intake.</p>
      <div class="sub">Story 2: Digital design</div>
      <p class="body">Another apprentice spends his time on digital models and simulation. His work is already saving his team time on new product trials.</p>
      <p class="body">The program gives him the chance to gain a degree without leaving the workforce or taking on large debt.</p>
    </div>
    <div class="num l">04</div><div class="folio" style="left:80px">The future of technology 2019 program</div>
  </div>
  <div class="page">
    <div class="photo" role="img" aria-label="Photo of apprentices working together at computers in a technology lab" style="left:30px;top:30px;width:440px;height:200px"></div>
    <div class="content" style="top:245px">
      <p class="body">Many of the apprentices came from school leaver groups, while others changed careers to join. All share a drive to work with new technology.</p>
      <p class="body">Host employers report stronger engagement and better retention compared with traditional graduate paths.</p>
      <div class="sub">Story 3: Future pathways</div>
      <p class="body">One of the pilot apprentices has already been offered a full time role at the end of his study. He credits the rotations with giving him a clear view of the whole business.</p>
    </div>
    <div class="folio r">The future of technology 2019 program</div><div class="num r">05</div>
  </div>
</section>

<!-- Spread 5 -->
<section class="spread" style="top:2540px">
  <div class="page">
    <div class="content" style="top:40px">
      <div class="h1">Why this Model?</div>
      <p class="body" style="margin-top:12px">The world of work is changing. The Australian workforce is not just moving to a more knowledge-based economy, it needs people with higher skills who can adapt as systems change.</p>
      <p class="body">Traditional pathways to higher qualifications often pull people out of the workforce for years. This model keeps them working and earning while they study.</p>
      <p class="body">Employers gain loyal staff with skills shaped around their own processes. Apprentices gain a recognised qualification and a clear career path.</p>
      <p class="body">The model also brings universities, training providers and industry closer together so that course content stays current and useful.</p>
      <p class="body">The Technology Higher Apprenticeship program offers a real alternative for school leavers who want both practical experience and a university level qualification.</p>
    </div>
    <div class="num l">06</div><div class="folio" style="left:80px">The future of technology 2019 program</div>
  </div>
  <div class="page">
    <div class="photo" role="img" aria-label="Photo of hands typing on a laptop keyboard" style="left:0;top:0;width:500px;height:250px"></div>
    <div style="position:absolute;right:40px;top:270px;width:200px;font-family:Montserrat,sans-serif;font-weight:600;font-size:14px;line-height:1.3;color:var(--orange)">"The Australian workforce needs to be more highly skilled than ever."</div>
    <div class="folio r">The future of technology 2019 program</div><div class="num r">07</div>
  </div>
</section>

<!-- Spread 6 -->
<section class="spread" style="top:3160px">
  <div class="page">
    <div class="content" style="top:35px">
      <div class="h1">Course Structure</div>
      <p class="body" style="margin-top:10px">The program runs over four years of part time study. In Years 1 and 2 apprentices complete a Diploma of Applied Technologies. In Years 3 and 4 they complete an Associate Degree with a partner university.</p>
      <div class="sub" style="font-size:14px;font-family:Montserrat,sans-serif">Units of study</div>
      <div class="bar">Years 1 and 2: Diploma Level</div>
      <div class="units">
        <div>Working in Industry 4.0</div><div>Apply design thinking methods</div>
        <div>Use digital technologies</div><div>Apply advanced manufacturing</div>
        <div>Problem solving skills</div><div>Implement a robotics system</div>
        <div>Apply knowledge of electrics</div><div>Work with sensors and data</div>
        <div>Introduction to 3D printing</div><div>Apply lean principles</div>
        <div>Manage workplace projects</div><div>Collaborate on design tasks</div>
      </div>
    </div>
    <div class="num l">08</div><div class="folio" style="left:80px">The future of technology 2019 program</div>
  </div>
  <div class="page">
    <div class="content" style="top:30px">
      <div class="bar" style="margin-top:0">Years 3 and 4: Associate Degree</div>
      <div class="units">
        <div>Modelling in Industry 4.0</div><div>Advanced digital systems</div>
        <div>Engineering with data</div><div>Professional practice</div>
        <div>Mechatronics and control</div><div>Industrial networks</div>
        <div>Systems design methods</div><div>Cyber-physical systems</div>
        <div>Software for industry</div><div>Applied research project</div>
        <div>Quality and compliance</div><div>Industry capstone unit</div>
      </div>
    </div>
    <div class="photo" role="img" aria-label="Photo of an industrial robot arm" style="left:30px;top:230px;width:210px;height:180px"></div>
    <div class="photo" role="img" aria-label="Photo of a 3D printer producing a part" style="left:260px;top:230px;width:210px;height:180px;background:linear-gradient(135deg,#6a7480,#b0b8c0)"></div>
    <div class="folio r">The future of technology 2019 program</div><div class="num r">09</div>
  </div>
</section>

</body>
</html>
```